Corvael Channel Partner Program Brochure

We need a full color brochure designed for our Channel Partner program. The program is intended to recruit agents to sell our services. There's a lot of information to be communicated and the final design should not look too text heavy.

About Corvael:
Founded in 2007, Corvael is a global BPO/KPO provider delivering superior managed services in the areas of Managed NOC & Network services, App Development, Service Provisioning, Finance & Accounting, Fraud & Security Management, and IP Support to telecommunications companies worldwide. The company consistently helps its clients to dramatically improve their financial performance through its highly specialized services. Corvael is headquartered in the Washington, D.C. area. For more information, visit http://www.corvael-example.com. Follow the company on Twitter @Corvael.

Target Market(s)

Agents in the U.S. selling telecom products and services.

Industry/Entity Type

Telecommunications

Requirements
Must have
• Brochure is a half fold and the template is attached. Good use of balance between imagery/graphic and text.

```html
<!DOCTYPE html>
<html lang="en">
<head>
<meta charset="utf-8">
<title>Corvael Channel Partner Program Brochure</title>
<link href="https://fonts.googleapis.com/css2?family=Roboto+Condensed:wght@300;400;700&display=swap" rel="stylesheet">
<style>
:root{
  --backdrop:#c9cacc;
  --red:#b5121b;
  --red-deep:#8e0d14;
  --red-light:#d4232b;
  --ink:#333;
  --muted:#6b6b6b;
  --paper:#ffffff;
  --pale:#f4c9cb;
  --photo-warm:#cfc4b8;
  --photo-cool:#c9d0d8;
}
*{margin:0;padding:0;box-sizing:border-box}
html,body{width:932px;height:1200px;overflow:hidden;background:var(--backdrop)}
body{position:relative;font-family:"Roboto Condensed",Arial,sans-serif;color:var(--ink)}
.panel{position:absolute}
.abs{position:absolute}
.brand{font-weight:700;letter-spacing:1px;color:var(--red)}
.brand--white{color:#fff}

/* cover spread */
.back-cover{left:48px;top:48px;width:418px;height:543px;
  background:linear-gradient(90deg,var(--red-deep) 0%,var(--red) 45%,var(--red-light) 100%)}
.find-more{left:44px;top:434px;width:100px;text-align:right;font-weight:300;font-size:19px;line-height:22px;color:var(--pale);text-transform:uppercase}
.back-brand{left:162px;top:436px;font-size:16px;line-height:18px}
.contact{left:162px;top:461px;font-size:8.5px;line-height:12px;color:#fff;white-space:nowrap}
.contact span{display:inline-block;width:33px}

.front-cover{left:466px;top:48px;width:421px;height:543px;overflow:hidden;background:var(--paper)}
.front-cover svg{position:absolute;left:0;top:0}
.front-brand{left:0;width:421px;top:70px;text-align:center;font-size:34px}
.cover-title{right:39px;top:390px;text-align:right;color:#fff;font-weight:700;font-size:23px;line-height:26px}
.cover-sub{right:39px;top:452px;text-align:right;color:var(--pale);font-weight:300;font-size:15px;line-height:18px;width:240px}

/* inner spread */
.inner-left{left:48px;top:620px;width:418px;height:544px;background:var(--paper)}
.inner-right{left:466px;top:620px;width:421px;height:544px;background:var(--paper)}
.photo{position:absolute}
.photo--office{left:21px;top:27px;width:193px;height:300px;background:linear-gradient(160deg,#e9e8e6,var(--photo-cool) 60%,#8d949c)}
.photo--couple{left:225px;top:369px;width:193px;height:164px;background:linear-gradient(150deg,#d9cfc2,var(--photo-warm) 55%,#6f7a8c)}
.photo--home{left:15px;top:28px;width:174px;height:340px;background:linear-gradient(170deg,#f3f2ee,#e4e2dc 55%,#b9a58e)}
.inner-brand{left:242px;top:31px;font-size:16px}
.heading{position:absolute;font-weight:700;font-size:13px;color:var(--red);text-transform:uppercase}
.heading--dark{color:#3a3a3a;font-size:13.5px}
.body{position:absolute;font-size:8.2px;line-height:10.6px;color:var(--muted);text-align:justify}
.body p+p{margin-top:10px}
.benefits{left:212px;top:82px;width:200px}
.benefit{margin-bottom:11px}
.benefit h3{font-weight:700;font-size:10.5px;color:var(--red);margin-bottom:2px}
.benefit li{list-style:none;font-size:8.2px;line-height:10.8px;color:var(--muted)}
.enroll li{list-style:none;font-size:8.2px;line-height:10.8px;color:var(--muted)}
.enroll li span{display:inline-block;width:16px}
.foot-gray{left:0;top:533px;width:225px;height:11px;background:#d8d8d8}
.foot-red{left:0;top:533px;width:421px;height:11px;background:var(--red)}
</style>
</head>
<body>

<section class="panel back-cover" aria-label="Back cover">
  <div class="abs find-more">Find<br>Out<br>More</div>
  <div class="abs brand brand--white back-brand">CORVAEL</div>
  <div class="abs contact">
    <div><span>Phone</span>+1.888.555.0142</div>
    <div><span>Online</span>www.corvael-example.com/channel-partners</div>
    <div><span>E-mail</span>info@corvael-example.com</div>
  </div>
</section>

<section class="panel front-cover" aria-label="Front cover">
  <svg width="421" height="543" viewBox="0 0 421 543">
    <defs>
      <linearGradient id="coverRed" x1="0" y1="0" x2="0" y2="1">
        <stop offset="0" stop-color="#c8161f"/>
        <stop offset="1" stop-color="#8e0d14"/>
      </linearGradient>
      <linearGradient id="sheen" x1="0" y1="0" x2="1" y2="0">
        <stop offset="0" stop-color="#f2f2f2"/>
        <stop offset="1" stop-color="#ffffff"/>
      </linearGradient>
    </defs>
    <rect width="421" height="543" fill="url(#sheen)"/>
    <path d="M0 175 Q210 150 421 170 L421 543 L0 543 Z" fill="url(#coverRed)"/>
    <path d="M0 176 Q190 120 421 164" fill="none" stroke="#1d1d1d" stroke-width="3"/>
  </svg>
  <div class="abs brand front-brand">CORVAEL</div>
  <h1 class="abs cover-title">CORVAEL CHANNEL<br>PARTNER PROGRAM</h1>
  <p class="abs cover-sub">A Program designed to make your partnership with Corvael highly productive and profitable</p>
</section>

<section class="panel inner-left" aria-label="Inside left page">
  <div class="photo photo--office" role="img" aria-label="Photo of two business colleagues working at a laptop in an office"></div>
  <div class="abs brand inner-brand">CORVAEL</div>
  <h2 class="heading" style="left:237px;top:78px">Overview</h2>
  <div class="body" style="left:237px;top:98px;width:168px">
    <p>The Corvael Partner Program is designed to make your partnership with Corvael highly productive and profitable. When you offer Corvael's best-in-class managed services to telco/cable service providers, you'll boost profitability and grow your business.</p>
    <p>Our success is based on yours and we are deeply committed to helping your business prosper.</p>
    <p>Corvael is a boutique managed services provider offering strategic sourcing solutions to communications companies worldwide. When you transfer your key internal functions to Corvael, you benefit from improved operational and financial performance, and increase your competitiveness and customer satisfaction through our broad services portfolio. With Corvael's telco experts managing your key OSS/BSS functions, you are now free to stay focused on sales and marketing activities to drive your company's growth.</p>
  </div>
  <h2 class="heading" style="left:32px;top:365px">Who is Corvael?</h2>
  <div class="body" style="left:32px;top:387px;width:181px">
    <p>Founded in 2007 and headquartered in the Washington, D.C. area, Corvael is a global BPO/KPO provider delivering superior managed services in the areas of Managed NOC &amp; Network services, App Development, Service Provisioning, Finance &amp; Accounting, Fraud &amp; Security Management, and IP Support to telecommunications companies worldwide. Corvael consistently helps its clients to dramatically improve their financial performance through its highly specialized services.</p>
  </div>
  <div class="photo photo--couple" role="img" aria-label="Photo of a couple working together at a laptop in a kitchen"></div>
  <div class="abs foot-gray"></div>
</section>

<section class="panel inner-right" aria-label="Inside right page">
  <div class="photo photo--home" role="img" aria-label="Photo of a man sitting on the floor at home using a laptop"></div>
  <h2 class="heading heading--dark" style="left:212px;top:55px">Why become a Corvael partner?</h2>
  <div class="abs benefits">
    <div class="benefit"><h3>Growth Opportunities</h3><ul>
      <li>Create competitive differentiation</li>
      <li>Offer greater range of products &amp; services</li>
      <li>Enhance &amp; expand relationship with clients</li>
      <li>Increase revenues, profitability, and success</li></ul></div>
    <div class="benefit"><h3>Financial Rewards</h3><ul>
      <li>Aggressive commissions earning potential</li>
      <li>Incentives &amp; promotions</li>
      <li>Earn an additional 5% on your monthly commissions for the first deal</li></ul></div>
    <div class="benefit"><h3>Best-in-Class Managed Services</h3><ul>
      <li>NOC &amp; network services</li>
      <li>Service delivery</li>
      <li>Finance &amp; accounting</li>
      <li>Fraud management</li>
      <li>App development</li>
      <li>IP Support</li></ul></div>
    <div class="benefit"><h3>Telco Experts</h3><ul>
      <li>Leading global telco focused MSP</li>
      <li>Decades of experience – telco is in our DNA</li>
      <li>Premier team of certified professionals</li>
      <li>Over 6 years of proven track record delivering operational &amp; financial performance</li></ul></div>
  </div>
  <h2 class="heading" style="left:51px;top:428px">Enrolling in the Corvael Channel Partner Program</h2>
  <ul class="abs enroll" style="left:51px;top:446px;width:330px">
    <li>Joining the Corvael Channel Partner Program is easy.</li>
    <li><span>1.</span>Visit www.corvael-example.com/channel-partners</li>
    <li><span>2.</span>Complete our online application form</li>
    <li><span>3.</span>Once your application is accepted and you are registered in the program, you will receive a welcome kit and access to sales information</li>
  </ul>
  <div class="abs foot-red"></div>
</section>

</body>
</html>
```